Verdant Wellness Compass Brochure for Conference Exhibit

We need a brochure design for our company, Verdant Wellness Compass. we have developed a web based patient assessment and management tool for providers treating Thyroid Disease and Bio-Identical Hormone Replacement Therapy. We would like a medical brochure that targets providers/practitioners and highlights the ease and efficiency of using our VWC Portal. I have attached a last-minute brochure we put together last year for reference and copy. we are open to color schemes that compliment our logo

Industry/Entity Type

It Company

```html
<!DOCTYPE html>
<html lang="en">
<head>
<meta charset="utf-8">
<title>Verdant Wellness Compass – Trifold Brochure</title>
<link href="https://fonts.googleapis.com/css2?family=Roboto:ital,wght@0,400;0,500;0,700;0,900;1,400;1,700&display=swap" rel="stylesheet">
<style>
:root{
  --bg:#e4e5e8;
  --navy:#26308a;
  --blue:#3346a8;
  --blue-light:#5a74c9;
  --sky:#2ea4dc;
  --ink:#2b2d3a;
  --muted:#555a6a;
  --paper:#f7f8fb;
  --paper-shade:#e3e7ef;
  --dark-band:#2c2f3b;
  --white:#ffffff;
}
*{box-sizing:border-box;margin:0;padding:0}
html,body{width:1000px;height:1200px;overflow:hidden}
body{background:var(--bg);font-family:"Roboto",Arial,sans-serif;color:var(--ink);position:relative}
.spread{position:absolute;left:140px;width:720px;height:556px;display:flex;box-shadow:0 6px 18px rgba(0,0,0,.18);background:var(--paper)}
.spread--outside{top:24px}
.spread--inside{top:620px}
.panel{position:relative;width:240px;height:100%;overflow:hidden;background:linear-gradient(180deg,var(--paper) 0%,var(--paper-shade) 100%)}
.panel + .panel{border-left:1px solid rgba(0,0,0,.08)}
.panel--wide{width:480px}
.band{position:absolute;left:0;width:100%;background:linear-gradient(135deg,var(--navy),var(--blue))}
.brand{font-weight:700;color:var(--white);letter-spacing:.5px}
.brand-mark{display:inline-block;width:12px;height:12px;border-radius:50%;background:var(--white);vertical-align:middle;margin-right:6px}
.h-title{color:var(--navy);font-weight:900;line-height:1.1}
.body-copy{font-size:7.6px;line-height:1.45;color:var(--muted)}
.bullets{list-style:none;font-size:8px;line-height:1.55;color:var(--ink)}
.bullets li{position:relative;padding-left:11px}
.bullets li::before{content:"";position:absolute;left:0;top:3.5px;width:6px;height:6px;border-radius:50%;background:var(--navy)}
.photo{position:absolute;left:0;width:100%}
.fold-shadow{position:absolute;top:0;bottom:0;width:18px;pointer-events:none}

/* outside: who */
.who__title{position:absolute;left:20px;top:26px;width:205px;font-size:20px}
.who__copy{position:absolute;left:20px;top:84px;width:205px}
.who__copy b{color:var(--ink)}
.who__quote{position:absolute;left:20px;top:198px;width:205px;font-style:italic;color:var(--blue);font-size:11px;line-height:1.3}
.who__quote cite{display:block;font-style:normal;font-weight:700;color:var(--navy);margin-top:6px;font-size:10.5px}
.who__photo{top:300px;height:256px;background:linear-gradient(180deg,#bcd4ea 0%,#6f9a63 45%,#4f7d3e 70%,#8cae5a 100%)}

/* outside: bhrt */
.bhrt__top{top:0;height:70px}
.pill{position:absolute;left:50%;transform:translateX(-50%);top:22px;padding:7px 20px;border-radius:20px;background:radial-gradient(circle at 50% 30%,var(--blue-light),var(--navy));border:2px solid var(--white);color:var(--white);font-weight:900;font-size:13px;white-space:nowrap}
.bhrt__copy{position:absolute;left:18px;top:82px;width:206px}
.bhrt__copy p{margin-bottom:6px}
.bhrt__copy .bullets{font-size:7.6px;margin:2px 0 7px}
.bhrt__bottom{top:412px;height:144px}
.bhrt__brand{position:absolute;left:20px;top:14px;font-size:26px}
.contact{position:absolute;left:14px;top:58px;width:212px}
.contact__pill{display:inline-flex;align-items:center;gap:5px;background:var(--white);color:var(--ink);border-radius:12px;padding:3px 10px;font-weight:900;font-size:11px}
.contact__line{color:#dfe4f6;font-size:7.4px;margin-top:5px}
.contact__web{color:var(--white);font-weight:700;font-size:11.5px;margin-top:6px}

/* outside: cover */
.cover__top{top:0;height:72px}
.cover__brand{position:absolute;left:22px;top:18px;display:flex;align-items:center;gap:10px}
.cover__brand .abbr{font-size:26px}
.cover__brand .full{font-size:10px;line-height:1.15;font-weight:700;color:var(--white)}
.cover__headline{position:absolute;left:22px;top:92px;width:200px;font-size:14.5px;color:var(--blue)}
.cover__photo{top:236px;height:232px;background:linear-gradient(160deg,#f4f6f8 0%,#d7dde6 45%,#9aa6b8 75%,#3a4256 100%)}
.cover__bottom{top:480px;height:76px}
.cover__web{position:absolute;left:0;right:0;top:46px;text-align:center;color:var(--white);font-weight:700;font-size:12px}

/* inside: benefits */
.benefits__top{top:0;height:58px}
.benefits__head{position:absolute;left:16px;top:14px;display:flex;align-items:center;gap:10px}
.benefits__head .abbr{font-size:20px}
.benefits__head .label{color:var(--white);font-weight:900;font-size:13px;line-height:1.05}
.benefits__list{position:absolute;left:18px;top:70px;width:210px}
.benefits__list h3{font-size:10.5px;color:var(--navy);font-weight:900;line-height:1.2;margin:9px 0 4px}
.benefits__list h3:first-child{margin-top:0}
.benefits__list .bullets{padding-left:8px}
.benefits__photo{top:420px;height:136px;background:linear-gradient(180deg,#f1f3f6 0%,#b9bec8 40%,#4c505b 80%,#2d3038 100%)}
.key-label{position:absolute;left:78px;top:48px;background:linear-gradient(180deg,var(--blue-light),var(--navy));color:var(--white);font-weight:700;font-size:14px;text-align:center;line-height:1.05;padding:7px 14px;border-radius:6px}

/* inside: features */
.why-top{top:0;height:54px;background:var(--dark-band)}
.why-top h2{position:absolute;left:24px;top:7px;color:var(--sky);font-size:11px;font-weight:900}
.why-top p{position:absolute;left:24px;top:22px;width:430px;font-size:7.2px;line-height:1.4;color:#cfd3de}
.features-bar{position:absolute;left:0;top:58px;width:100%;height:36px;background:linear-gradient(90deg,var(--navy) 0%,var(--blue-light) 55%,rgba(90,116,201,0) 100%)}
.features-bar .title{position:absolute;left:24px;top:9px;display:flex;align-items:center;gap:8px}
.features-bar .abbr{font-size:16px}
.features-bar .label{color:var(--white);font-weight:900;font-size:13px}
.feature-col{position:absolute}
.feature-col h4{font-size:8.6px;color:var(--navy);font-weight:700;margin-bottom:3px}
.feature-col .bullets{font-size:7.5px}
.col-workflow{left:24px;top:104px;width:140px}
.col-consult{left:24px;top:226px;width:140px}
.col-lab{left:174px;top:170px;width:120px}
.col-info{left:342px;top:162px;width:120px}
.login-box{position:absolute;left:174px;top:100px;width:120px;height:62px;border-radius:3px;background:linear-gradient(180deg,var(--blue-light),var(--navy));box-shadow:0 2px 5px rgba(0,0,0,.25)}
.secure-note{position:absolute;left:300px;top:104px;width:88px;font-size:6.2px;line-height:1.35;color:var(--muted)}
.partner-badge{position:absolute;left:396px;top:118px;width:54px;height:18px;border-radius:3px;background:#b8bdc8}
.quote-bubble{position:absolute;left:174px;top:232px;width:222px;padding:7px 10px;border-radius:12px;background:var(--sky);color:var(--white);font-size:8px;font-style:italic;line-height:1.35}
.quote-bubble cite{display:block;text-align:right;font-size:6.6px;font-style:normal;font-weight:700;margin-top:2px}
.quote-bubble::after{content:"";position:absolute;right:30px;bottom:-8px;border:8px solid transparent;border-top-color:var(--sky);border-bottom:0}
.woman-photo{position:absolute;left:384px;top:262px;width:96px;height:138px;background:linear-gradient(180deg,rgba(255,255,255,0) 0%,#e6e9ef 40%,#cfd4de 100%)}
.why-copy{position:absolute;left:24px;top:300px;width:360px}
.why-copy h3{font-size:10.5px;color:var(--navy);font-weight:900;margin-bottom:4px}
.why-copy p{margin-bottom:8px}
.inside-bottom{top:520px;height:36px}
</style>
</head>
<body>

<!-- OUTSIDE SPREAD -->
<section class="spread spread--outside" aria-label="Brochure outside">
  <article class="panel who">
    <h2 class="h-title who__title">Who is Verdant Wellness Compass?</h2>
    <p class="body-copy who__copy"><b>Verdant Wellness Compass (VWC)</b> is committed to advancing the practice of balanced Bio-Identical Hormone Replacement Therapy (BHRT) and Thyroid Therapy to help providers deliver a higher quality of care. VWC developed a web-based patient assessment and management software that provides BHRT practitioners with a proven workflow template, assessment tools and compound friendly e-prescribing portal.</p>
    <blockquote class="who__quote">“We age because our hormones decline, our hormones don’t decline because we age.”
      <cite>Dana Whitfield, MD</cite>
    </blockquote>
    <div class="photo who__photo" role="img" aria-label="Photo of a smiling couple outdoors on a sunny lawn with trees"></div>
  </article>

  <article class="panel bhrt">
    <svg class="band bhrt__top" viewBox="0 0 240 70" preserveAspectRatio="none" style="background:none" aria-hidden="true">
      <path d="M0 0H240V48Q120 78 0 52Z" fill="#26308a"/>
    </svg>
    <div class="pill">WHAT IS BHRT</div>
    <div class="body-copy bhrt__copy">
      <p>Practitioners of Bio-Identical Hormone Therapy (BHRT) prescribe hormones that are structurally and functionally identical to those naturally found in the human body.</p>
      <p>Experts believe maintaining the balanced actions of these hormones may slow the effects of aging on the body. These hormones are custom dosed to each patient after a thorough evaluation of the most beneficial outcome. Typically including:</p>
      <ul class="bullets">
        <li>Patient medical history</li>
        <li>Personal and familial risk factors</li>
        <li>Social variables</li>
        <li>Current medications and supplements</li>
        <li>Evaluation of symptoms including those specific to individual hormones, thyroid and adrenal function</li>
      </ul>
      <p>A clinical picture is formed, then the practitioner validates the findings with lab testing and personal review.</p>
      <p>Finally, armed with this information, the proper dosage of bio-identical hormones is prescribed to restore the balance, followed by ongoing monitoring and adjustment so hormone and thyroid levels stay optimal.</p>
    </div>
    <div class="band bhrt__bottom">
      <div class="brand bhrt__brand"><span class="brand-mark"></span>VWC</div>
      <div class="contact">
        <span class="contact__pill">
          <svg width="10" height="10" viewBox="0 0 24 24" aria-hidden="true"><path fill="#26308a" d="M6.6 10.8a15 15 0 006.6 6.6l2.2-2.2a1 1 0 011-.25 11.4 11.4 0 003.6.6 1 1 0 011 1V20a1 1 0 01-1 1A17 17 0 013 4a1 1 0 011-1h3.5a1 1 0 011 1c0 1.25.2 2.45.6 3.6a1 1 0 01-.25 1z"/></svg>
          Contact Us: 555-214-0386</span>
        <div class="contact__line">info@verdantwellnesscompass.com</div>
        <div class="contact__line">1180 Larkspur Way, Suite 200, Fairhaven, TX 75001</div>
        <div class="contact__web">www.verdantwellnesscompass.com</div>
      </div>
    </div>
  </article>

  <article class="panel cover">
    <div class="band cover__top">
      <div class="cover__brand"><span class="brand abbr"><span class="brand-mark"></span>VWC</span><span class="full">Verdant<br>Wellness<br>Compass</span></div>
    </div>
    <h1 class="h-title cover__headline">Web-Based Patient Assessment &amp; Management Software for Use by Integrated Medicine Providers to Advance the Practice of Balanced BHRT and Thyroid Therapy</h1>
    <div class="photo cover__photo" role="img" aria-label="Photo of a physician at a desk pointing to a laptop screen in a bright office"></div>
    <div class="band cover__bottom"><div class="cover__web">www.verdantwellnesscompass.com</div></div>
  </article>
</section>

<!-- INSIDE SPREAD -->
<section class="spread spread--inside" aria-label="Brochure inside">
  <article class="panel benefits">
    <div class="band benefits__top">
      <div class="benefits__head"><span class="brand abbr"><span class="brand-mark"></span>VWC</span><span class="label">SYSTEM<br>BENEFITS</span></div>
    </div>
    <div class="benefits__list">
      <h3>Increase Efficiency in BHRT Patient Case Management</h3>
      <ul class="bullets">
        <li>Automated Patient Data Compilation</li>
        <li>Patient Data Organized in Detailed Report</li>
        <li>Delegate More Tasks</li>
        <li>24-Hour Web Access</li>
      </ul>
      <h3>Treat BHRT Patients with increased Confidence</h3>
      <ul class="bullets">
        <li>Physician Access to BHRT Specialist for Patient Cases</li>
        <li>Improve Patient Outcomes</li>
        <li>Decrease Patient Turnover</li>
        <li>Proven BHRT Workflow Template</li>
      </ul>
      <h3>Increase Patient Confidence in Provider</h3>
      <ul class="bullets">
        <li>Personalized Case Management</li>
        <li>Increased Patient-Provider Communication</li>
        <li>Improved Patient Education of Therapy and Goals</li>
        <li>Electronic Capabilities Improve Patient’s Perception of Professionalism</li>
      </ul>
    </div>
    <div class="photo benefits__photo" role="img" aria-label="Close-up photo of a computer keyboard">
      <div class="key-label">Improve<br>efficiency</div>
    </div>
  </article>

  <article class="panel panel--wide features">
    <div class="band why-top">
      <h2>WHY IS HORMONE BALANCE IMPORTANT?</h2>
      <p>The art of using Bio-Identical Hormone Replacement Therapy (BHRT) to balance and maintain the actions of human hormones at more healthy and vigorous levels can improve patient symptoms, health markers, and overall quality of life.</p>
    </div>
    <div class="features-bar"><div class="title"><span class="brand abbr"><span class="brand-mark"></span>VWC</span><span class="label">SYSTEM FEATURES</span></div></div>

    <div class="feature-col col-workflow">
      <h4>BHRT Case Workflow</h4>
      <ul class="bullets">
        <li>Electronic Collection of Patient Info</li>
        <li>Relevant Medical History</li>
        <li>Risk Factors</li>
        <li>Symptom Survey</li>
        <li>Assessment Summary</li>
        <li>Hormone Balance Interpretation</li>
        <li>Lab Panel Recommendations</li>
        <li>Symptom Progression Results Grid</li>
      </ul>
    </div>
    <div class="feature-col col-consult">
      <h4>Consultation with BHRT Specialist</h4>
      <ul class="bullets">
        <li>Record Ordered Lab Panels</li>
        <li>Comparative Results Report</li>
        <li>Serum, Saliva, Blood Spot, Urine</li>
      </ul>
    </div>
    <div class="login-box" role="img" aria-label="Screenshot of the VWC Portal login form"></div>
    <p class="secure-note">The VWC web portal is encrypted with the highest level of security and is full compliance with HIPAA Privacy Protection.</p>
    <div class="partner-badge" aria-hidden="true"></div>
    <div class="feature-col col-lab">
      <h4>Lab Functionality</h4>
      <ul class="bullets">
        <li>Record Ordered Lab Panels</li>
        <li>Comparative Results Report</li>
        <li>Serum, Saliva, Blood Spot, Urine</li>
      </ul>
    </div>
    <div class="feature-col col-info">
      <h4>Informational Database</h4>
      <ul class="bullets">
        <li>BHRT Educational Studies and Papers</li>
        <li>BHRT Clinical Tips</li>
      </ul>
    </div>
    <blockquote class="quote-bubble">“A woman can only feel optimal when all of her different hormones reflect a balance of actions in the body”
      <cite>Dr. Marcus Ellery, MD (2011) “Clinical Endocrine Practice Guide”</cite>
    </blockquote>
    <div class="woman-photo" role="img" aria-label="Photo of an energetic woman in white raising her arm"></div>
    <div class="body-copy why-copy">
      <h3>Why VWC Patient Assessment and Management Software?</h3>
      <p>For experienced BHRT practitioners, the VWC Software’s electronic capabilities provide for greater task delegation and improved efficiency. The software’s educational database and clinical tips benefit those newer to BHRT by improving skill and efficacy in patient treatment while increasing provider confidence.</p>
      <p>Under the care of VWC physicians, compliant patients experience satisfaction rates of greater than 90%. Satisfied patients translate into loyal patients continuing to seek optimum outcomes. With increased patient retention, physicians realize a more prosperous and sustainable practice.</p>
    </div>
    <div class="band inside-bottom"></div>
  </article>
</section>

</body>
</html>
```